Webshop for furniture and lamps

We need a design for a web shop with APP that should have two options:
1-Webshop in general which should attract to private customer in general and
2-Website that is meant to attract big customers as hotels and restaurants who would have their own customerize login.

That's the idea behind the shop.

It should be diveded into 4 parts
vintage furniture
rattan set outdoor and indoor
lamps and
wooden wall decor

The name of the shop is borgo veneria!

Please kindly make me an offer.

Reason: Dear designers, so far there hasn't been a design that really matched. Look up German web sites like www.trevolind.de or www.quandor17.de... Haven't been convinced by designs! Sorry folks. Please submit some new ones. Kind regards Tam

```html
<!DOCTYPE html>
<html lang="en">
<head>
<meta charset="utf-8">
<title>borgo veneria – Furniture &amp; Lamps</title>
<link href="https://fonts.googleapis.com/css2?family=Open+Sans:wght@400;600;700&family=Oswald:wght@400;500&display=swap" rel="stylesheet">
<style>
:root{
  --orange:#f0932a;
  --dark:#3d3c3b;
  --darker:#2f2e2d;
  --topbar:#4a4948;
  --text:#555;
  --muted:#999;
  --price:#e3463b;
  --line:#e2e2e2;
  --page:#f4f4f4;
  --white:#fff;
}
*{box-sizing:border-box;margin:0;padding:0}
html,body{width:1200px;height:2424px;overflow:hidden}
body{font-family:'Open Sans',Arial,sans-serif;color:var(--text);background:var(--page);position:relative}
.abs{position:absolute}

.topbar{top:0;left:0;width:1200px;height:32px;background:var(--topbar);color:#ddd;font-size:12px}
.topbar .welcome{left:80px;top:8px}
.topbar .account{right:80px;top:8px;display:flex;gap:22px}

.header{top:32px;left:0;width:1200px;height:128px;background:var(--white)}
.brand{left:80px;top:42px;display:flex;align-items:center;gap:14px}
.brand-mark{width:40px;height:40px;background:var(--dark)}
.brand-name{font-family:'Oswald',sans-serif;font-size:34px;font-weight:500;color:var(--dark);letter-spacing:1px;text-transform:uppercase}
.nav{left:436px;top:56px;display:flex;gap:26px;font-size:14px;font-weight:700;color:var(--dark)}
.search{left:920px;top:50px;width:200px;height:30px;border:1px solid var(--line);border-radius:3px;font-size:12px;color:var(--muted);padding:6px 10px}

.hero{top:160px;left:0;width:1200px;height:368px;background:linear-gradient(90deg,#8a6d55 0%,#b58d6a 35%,#d9c6b0 55%,#5d4a3c 100%)}
.hero-panel{right:0;top:0;width:380px;height:368px;background:rgba(40,38,36,.72);color:#fff;padding:80px 60px 0 40px;text-align:right}
.hero-panel h1{font-family:'Oswald',sans-serif;font-weight:500;font-size:44px;letter-spacing:1px}
.hero-panel p{font-size:12px;line-height:20px;margin-top:14px;color:#e4e4e4}
.btn-outline{display:inline-block;border:2px solid #fff;color:#fff;font-size:14px;font-weight:700;padding:8px 18px;margin-top:22px}

.section-tab{background:var(--dark);color:#fff;font-size:14px;font-weight:700;padding:12px 18px}
.featured-tab{left:80px;top:560px}

.card{width:240px;background:var(--white);box-shadow:0 1px 5px rgba(0,0,0,.15);text-align:center}
.card .photo{margin:20px auto 0;width:180px;height:170px;border-radius:4px}
.card h3{font-size:13px;font-weight:700;color:var(--dark);margin-top:38px}
.card p{font-size:10px;color:var(--muted);line-height:14px;margin:8px 22px 0}
.card .price{font-size:24px;font-weight:700;color:var(--price);margin-top:8px}
.card .actions{display:flex;justify-content:center;gap:8px;margin-top:16px}
.btn-buy{border:1px solid #bbb;font-size:11px;font-weight:600;color:var(--dark);padding:6px 18px}
.btn-cart{width:32px;height:28px;background:var(--orange);display:flex;align-items:center;justify-content:center}

.banner{left:80px;top:1480px;width:1040px;height:132px;background:linear-gradient(90deg,#c8d4dc 0%,#7a9bb0 30%,#d4b89a 55%,#8aa5b0 75%)}
.banner-text{right:0;top:0;width:300px;height:132px;background:rgba(120,140,120,.55);color:#fff;padding:32px 30px}
.banner-text h2{font-family:'Oswald',sans-serif;font-weight:400;font-size:34px;line-height:38px}
.banner-text span{font-size:11px}

.col-title{top:1660px}
.blog-post{width:320px}
.blog-post h4{font-size:12px;font-weight:700;color:var(--dark)}
.blog-post .date{font-size:10px;color:var(--muted);margin-top:6px}
.blog-post p{font-size:11px;line-height:17px;margin-top:8px}
.blog-post .more{font-size:10px;color:var(--muted);margin-top:8px}
.tweet{width:308px;display:flex;gap:14px}
.tweet .avatar{width:56px;height:56px;border-radius:50%;background:#c9c2ba;flex:none}
.tweet b{font-size:11px;color:var(--dark)}
.tweet b em{font-style:normal;color:var(--orange);font-weight:600}
.tweet p{font-size:10px;line-height:15px;margin-top:4px}
.tweet small{display:block;font-size:10px;color:var(--muted);margin-top:6px}
.video{left:812px;top:1720px;width:308px;height:250px;background:linear-gradient(135deg,#8a7a68,#5f5448 60%,#a79784)}

.footer{top:2040px;left:0;width:1200px;height:320px;background:var(--dark);color:#bbb}
.fcol h5{font-size:13px;font-weight:700;color:#fff;margin-bottom:22px}
.fcol li{list-style:none;font-size:11px;line-height:22px}
.fcol p{font-size:11px;line-height:18px}
.cards{display:flex;gap:8px;margin-top:20px}
.cards span{width:38px;height:24px;background:#fff;border-radius:2px}
.signup{display:flex;margin-top:20px}
.signup span{width:150px;height:32px;background:#fff;font-size:10px;color:var(--muted);padding:9px}
.signup b{width:64px;height:32px;background:var(--orange);color:#fff;font-size:11px;padding:9px 10px}

.bottombar{top:2360px;left:0;width:1200px;height:64px;background:var(--darker);color:#aaa;font-size:11px}
.bottombar .copy{left:80px;top:24px}
.bottombar .links{left:500px;top:24px;display:flex;gap:24px}
.bottombar .social{right:80px;top:20px;display:flex;gap:8px}
.bottombar .social span{width:24px;height:24px;border-radius:50%;background:#777}
</style>
</head>
<body>

<div class="topbar abs">
  <div class="welcome abs">Lena Morvik, welcome to our online store!</div>
  <div class="account abs"><span>Setting</span><span>My Account</span><span>Cart 0 item</span></div>
</div>

<header class="header abs">
  <div class="brand abs"><span class="brand-mark"></span><span class="brand-name">borgo veneria</span></div>
  <nav class="nav abs"><span>HOME</span><span>CATEGORIES</span><span>ABOUT US</span><span>FAQs</span><span>CONTACT US</span></nav>
  <div class="search abs">Search entire store here</div>
</header>

<section class="hero abs" role="img" aria-label="Bedroom interior with bed, bedside lamp and wooden wall">
  <div class="hero-panel abs">
    <h1>LOREM IPSUMEI</h1>
    <p>Vintage pieces, rattan sets, lamps and wooden wall decor selected for homes, hotels and restaurants.</p>
    <span class="btn-outline">VIEW MORE</span>
  </div>
</section>

<div class="section-tab featured-tab abs">FEATURED PRODUCTS</div>

<!-- product cards -->
<div class="card abs" style="left:80px;top:628px;height:404px"><div class="photo" role="img" aria-label="Painted vintage chest of drawers" style="background:linear-gradient(135deg,#b2473a,#5f7a8e)"></div><h3>VOLUPTATEM FUGIT AUT</h3><p>Solid wood piece with hand painted drawers and brass handles.</p><div class="price">$856.00</div><div class="actions"><span class="btn-buy">BUY NOW</span><span class="btn-cart"><svg width="16" height="14" viewBox="0 0 16 14"><path d="M1 1h3l2 8h8l1-6H5" fill="none" stroke="#fff" stroke-width="1.6"/><circle cx="7" cy="12" r="1.3" fill="#fff"/><circle cx="13" cy="12" r="1.3" fill="#fff"/></svg></span></div></div>
<div class="card abs" style="left:348px;top:628px;height:404px"><div class="photo" role="img" aria-label="Rustic wooden console table" style="background:linear-gradient(180deg,#f5f5f5 30%,#8b6a4e 45%,#f5f5f5 80%)"></div><h3>VOLUPTATEM FUGIT AUT</h3><p>Reclaimed timber table with a warm natural oiled finish.</p><div class="price">$856.00</div><div class="actions"><span class="btn-buy">BUY NOW</span><span class="btn-cart"><svg width="16" height="14" viewBox="0 0 16 14"><path d="M1 1h3l2 8h8l1-6H5" fill="none" stroke="#fff" stroke-width="1.6"/><circle cx="7" cy="12" r="1.3" fill="#fff"/><circle cx="13" cy="12" r="1.3" fill="#fff"/></svg></span></div></div>
<div class="card abs" style="left:612px;top:628px;height:404px"><div class="photo" role="img" aria-label="Dark rattan dining set" style="background:radial-gradient(circle,#4a4a4a 30%,#f5f5f5 70%)"></div><h3>VOLUPTATEM FUGIT AUT</h3><p>Woven rattan table and chairs for indoor or outdoor use.</p><div class="price">$856.00</div><div class="actions"><span class="btn-buy">BUY NOW</span><span class="btn-cart"><svg width="16" height="14" viewBox="0 0 16 14"><path d="M1 1h3l2 8h8l1-6H5" fill="none" stroke="#fff" stroke-width="1.6"/><circle cx="7" cy="12" r="1.3" fill="#fff"/><circle cx="13" cy="12" r="1.3" fill="#fff"/></svg></span></div></div>
<div class="card abs" style="left:880px;top:628px;height:404px"><div class="photo" role="img" aria-label="Tall weathered vintage cabinet" style="background:linear-gradient(90deg,#f5f5f5 25%,#7d5a3e 35%,#a4744c 65%,#f5f5f5 75%)"></div><h3>VOLUPTATEM FUGIT AUT</h3><p>Tall cabinet with open shelves and an aged patina surface.</p><div class="price">$856.00</div><div class="actions"><span class="btn-buy">BUY NOW</span><span class="btn-cart"><svg width="16" height="14" viewBox="0 0 16 14"><path d="M1 1h3l2 8h8l1-6H5" fill="none" stroke="#fff" stroke-width="1.6"/><circle cx="7" cy="12" r="1.3" fill="#fff"/><circle cx="13" cy="12" r="1.3" fill="#fff"/></svg></span></div></div>

<div class="card abs" style="left:80px;top:1060px;height:372px"><div class="photo" role="img" aria-label="Round rattan lounge set" style="background:radial-gradient(circle,#b58152 35%,#f5f5f5 70%)"></div><h3 style="margin-top:22px">VOLUPTATEM FUGIT AUT</h3><p>Round rattan lounge with soft cream seat cushions.</p><div class="price">$856.00</div><div class="actions"><span class="btn-buy">BUY NOW</span><span class="btn-cart"><svg width="16" height="14" viewBox="0 0 16 14"><path d="M1 1h3l2 8h8l1-6H5" fill="none" stroke="#fff" stroke-width="1.6"/><circle cx="7" cy="12" r="1.3" fill="#fff"/><circle cx="13" cy="12" r="1.3" fill="#fff"/></svg></span></div></div>
<div class="card abs" style="left:348px;top:1060px;height:372px"><div class="photo" role="img" aria-label="Colourful vintage sideboard" style="background:linear-gradient(135deg,#9b6b45,#5d8a8c 50%,#b8874f)"></div><h3 style="margin-top:22px">VOLUPTATEM FUGIT AUT</h3><p>Low sideboard built from painted reclaimed wood boards.</p><div class="price">$856.00</div><div class="actions"><span class="btn-buy">BUY NOW</span><span class="btn-cart"><svg width="16" height="14" viewBox="0 0 16 14"><path d="M1 1h3l2 8h8l1-6H5" fill="none" stroke="#fff" stroke-width="1.6"/><circle cx="7" cy="12" r="1.3" fill="#fff"/><circle cx="13" cy="12" r="1.3" fill="#fff"/></svg></span></div></div>
<div class="card abs" style="left:612px;top:1060px;height:372px"><div class="photo" role="img" aria-label="Floor lamp with beige shade" style="background:linear-gradient(180deg,#e8cf8e 0%,#f5f5f5 35%,#f5f5f5 100%)"></div><h3 style="margin-top:22px">VOLUPTATEM FUGIT AUT</h3><p>Slim floor lamp with a linen shade and brass stand.</p><div class="price">$856.00</div><div class="actions"><span class="btn-buy">BUY NOW</span><span class="btn-cart"><svg width="16" height="14" viewBox="0 0 16 14"><path d="M1 1h3l2 8h8l1-6H5" fill="none" stroke="#fff" stroke-width="1.6"/><circle cx="7" cy="12" r="1.3" fill="#fff"/><circle cx="13" cy="12" r="1.3" fill="#fff"/></svg></span></div></div>
<div class="card abs" style="left:880px;top:1060px;height:372px"><div class="photo" role="img" aria-label="Dark wooden cabinet with carved doors" style="background:linear-gradient(180deg,#f5f5f5 10%,#5a3a26 25%,#6e4a30 85%,#f5f5f5 95%)"></div><h3 style="margin-top:22px">VOLUPTATEM FUGIT AUT</h3><p>Carved wooden cabinet with two doors and inner shelf.</p><div class="price">$856.00</div><div class="actions"><span class="btn-buy">BUY NOW</span><span class="btn-cart"><svg width="16" height="14" viewBox="0 0 16 14"><path d="M1 1h3l2 8h8l1-6H5" fill="none" stroke="#fff" stroke-width="1.6"/><circle cx="7" cy="12" r="1.3" fill="#fff"/><circle cx="13" cy="12" r="1.3" fill="#fff"/></svg></span></div></div>

<section class="banner abs" role="img" aria-label="Outdoor lounge furniture with blue cushions on a terrace">
  <div class="banner-text abs"><h2>outside furniture</h2><span>Rattan sets for garden and terrace</span></div>
</section>

<div class="section-tab col-title abs" style="left:80px">LATES FROM BLOG</div>
<div class="section-tab col-title abs" style="left:452px">TWEETS</div>
<div class="section-tab col-title abs" style="left:812px">WATCH VIDEO</div>

<article class="blog-post abs" style="left:80px;top:1730px"><h4>LOREM IPSUM DOLOR SIT AMET NON EGO</h4><div class="date">May 30, 2015</div><p>Fresh ideas for mixing vintage wood with rattan in a bright living room setting.</p><div class="more">read more</div></article>
<article class="blog-post abs" style="left:80px;top:1860px"><h4>LOREM IPSUM DOLOR SIT AMET NON EGO</h4><div class="date">May 30, 2015</div><p>How hotels and restaurants choose lamps that set a warm and calm evening mood.</p><div class="more">read more</div></article>

<div class="tweet abs" style="left:452px;top:1730px"><span class="avatar"></span><div><b>Marco Ferri <em>@borgoveneria</em></b><p>New rattan lounge sets just arrived in the shop. Ready for the summer terrace season.</p><small>Retweeted by Elio Brandt</small></div></div>
<div class="tweet abs" style="left:452px;top:1860px"><span class="avatar"></span><div><b>Marco Ferri <em>@borgoveneria</em></b><p>Our wooden wall decor pieces are hand finished and each one is a little different.</p><small>Retweeted by Elio Brandt</small></div></div>

<div class="video abs" role="img" aria-label="Video still of a rustic wooden sideboard in a room">
  <svg class="abs" style="left:122px;top:93px" width="64" height="64" viewBox="0 0 64 64"><circle cx="32" cy="32" r="32" fill="#fff"/><path d="M26 20l18 12-18 12z" fill="#3d3c3b"/></svg>
</div>

<footer class="footer abs">
  <div class="fcol abs" style="left:80px;top:44px"><h5>COMPANY</h5><ul><li>Search</li><li>About</li><li>News</li><li>Reviews</li><li>Contact Us</li></ul></div>
  <div class="fcol abs" style="left:250px;top:44px"><h5>SHIPPING</h5><ul><li>Shipping Fee</li><li>Order and Returns</li><li>Track Order</li><li>Secure Shop</li><li>Site Map</li></ul></div>
  <div class="fcol abs" style="left:430px;top:44px"><h5>FAQs</h5><ul><li>Customer Service</li><li>Privacy Policy</li><li>Terms of Use</li><li>My Account</li><li>Hotels</li></ul></div>
  <div class="fcol abs" style="left:608px;top:44px;width:200px"><h5>PAYMENT METHOD</h5><p>Pay safely by card, transfer or invoice for business clients with their own login.</p><div class="cards"><span></span><span></span><span></span><span></span></div></div>
  <div class="fcol abs" style="left:880px;top:44px;width:240px"><h5>NEWS &amp; UPDATES</h5><p>Sign up to get the latest news, new arrivals and offers.</p><div class="signup"><span>Your email</span><b>SIGN UP</b></div></div>
</footer>

<div class="bottombar abs">
  <div class="copy abs">© 2015 Your Company</div>
  <div class="links abs"><span>About us</span><span>privacy policy</span><span>terms and use</span><span>Careers</span><span>Countries</span><span>contact us</span></div>
  <div class="social abs"><span></span><span></span><span></span><span></span><span></span></div>
</div>

</body>
</html>
```